Landing Page that will convert (Design Only Landing Page Project)

I am looking for a design that will resonate with a dentist, doctor or anyone business owner in the medical field. My goal is to have then scheduled a 15 min session with me at the end to discuss how I can help then meet there financial goals (short or long term)

I am open to all design concepts and suggestions as far as the important contents or links that should be on the page (ie. Main menu like, Home, About, Services, Schedule, Contact Us).

There is no right or wrong answer, just need a great accounting/financing landing page. Again the project is for just the design of the page, and coding will be done elsewhere.

Target Market(s)

medical professionals, this includes small business owners of privately held office suck as medical doctors, dentist, ophthalmologist, chiropractors, etc

Industry/Entity Type

Finance And Accounting

Colors
fdfdfd
1b1b1b
f3f1f8
e4daeb

Requirements
Must have
• The goal of this landing page is to have the visitor schedule a 15min discovery call, therefore, a calender scheduling option is ideal, so we can understand their goals and see what obstacles they are facing and therefore avoid those obstacles before they become a burden
Nice to have
• A video background or maybe a medical professional office in that way they feel connected. For design purposes just use a video/image placeholder. I feel more is less if we can research some of the most successful landing page design and incorporate some of those elements that would to great.
• I saw this example and thought it was ok
• https://www.plovanet.com/#features
• WHAT I LIKE ABOUT THIS DESIGN:
• - It's simple, clean,
• - font is readable,
• - like the illustration
• - elegance
• - It clearly defines what the use should do, its intuitive, walks the user to the bottom of the page and give them the option of whether to signup or exit the page.

```html
<!DOCTYPE html>
<html lang="en">
<head>
<meta charset="utf-8">
<title>Steady Ledger — Financial Guidance for Medical Practices</title>
<link href="https://fonts.googleapis.com/css2?family=Poppins:wght@400;500&family=Open+Sans:wght@400;600&display=swap" rel="stylesheet">
<style>
  :root{
    --ink:#1b1b1b;
    --paper:#fdfdfd;
    --lilac-soft:#ece7f5;
    --lilac:#e4daeb;
    --lilac-button:#dccbe8;
    --purple:#a55fd2;
    --purple-deep:#3a1650;
    --purple-bright:#6b2a9c;
    --header:#0b0b0f;
    --footer:#262626;
    --body-text:#444;
    --muted:#777;
    --line:#cfcfcf;
  }
  *{box-sizing:border-box;margin:0;padding:0}
  html,body{width:1200px;height:2525px;overflow:hidden;background:var(--paper)}
  body{font-family:"Open Sans",Arial,sans-serif;color:var(--ink);position:relative}
  .page{position:relative;width:1200px;height:2525px}

  /* header */
  .site-header{position:absolute;top:0;left:0;width:1200px;height:98px;background:var(--header)}
  .brand{position:absolute;left:135px;top:28px;font-family:"Poppins",sans-serif;font-size:34px;font-weight:400;color:#7a3f9e;letter-spacing:-.5px;line-height:40px}
  .main-nav{position:absolute;right:133px;top:39px;display:flex;gap:30px;font-size:14px;line-height:20px}
  .main-nav a{color:#fff;text-decoration:none}
  .main-nav a.is-active{color:var(--purple)}

  /* hero */
  .hero{position:absolute;top:98px;left:0;width:1200px;height:518px;
    background:linear-gradient(100deg,#8f959c 0%,#b9bec4 35%,#9aa3ad 60%,#6f7a86 100%)}
  .hero-play{position:absolute;left:570px;top:199px}
  .hero-title{position:absolute;top:262px;left:0;width:1200px;text-align:center;font-family:"Poppins",sans-serif;font-weight:400;font-size:42px;color:#fff;line-height:60px}

  /* welcome */
  .welcome-title{position:absolute;left:133px;top:687px;font-family:"Poppins",sans-serif;font-weight:500;font-size:33px;color:var(--purple);line-height:44px}
  .welcome-text{position:absolute;left:133px;top:738px;width:455px;font-size:12.6px;line-height:22.3px;color:var(--body-text)}
  .btn-soft{display:block;position:absolute;background:var(--lilac-button);color:#5a2a7e;font-size:12px;text-transform:uppercase;text-align:center;line-height:37px;height:37px;width:100px;text-decoration:none}
  .welcome-btn{left:133px;top:892px}
  .welcome-photo{position:absolute;left:626px;top:695px;width:441px;height:234px;
    background:linear-gradient(90deg,#cfd8d8 0%,#e6ecec 50%,#aab7bb 100%)}

  /* services */
  .services{position:absolute;top:1010px;left:0;width:1200px;height:362px;background:var(--lilac-soft)}
  .section-title{position:absolute;left:0;width:1200px;text-align:center;font-family:"Poppins",sans-serif;font-weight:500;font-size:33px;color:var(--purple);line-height:44px}
  .services .section-title{top:70px}
  .service{position:absolute;top:135px;width:210px;text-align:center}
  .service svg{display:block;margin:0 auto}
  .service-name{font-family:"Poppins",sans-serif;font-weight:400;font-size:19px;margin-top:10px;line-height:26px;color:var(--ink)}
  .service-text{font-size:11.5px;line-height:19px;color:#555;margin-top:4px}

  /* testimonials */
  .testimonials .section-title{top:1442px}
  .testimonial{position:absolute;top:1508px;width:295px;height:283px;border:1px solid var(--line);background:#fff;text-align:center}
  .avatar{width:84px;height:84px;border-radius:50%;margin:27px auto 0;background:linear-gradient(160deg,#c9c9c9,#6f6f6f)}
  .quote{font-size:12.3px;line-height:21px;color:#555;margin:22px 28px 0}
  .author{font-family:"Poppins",sans-serif;font-weight:500;font-size:14.5px;margin-top:10px;line-height:20px}
  .author-role{font-size:11px;color:#444;line-height:16px}
  .view-all{left:550px;top:1824px;height:39px;line-height:39px}

  /* schedule */
  .schedule{position:absolute;top:1944px;left:0;width:1200px;height:466px;
    background:linear-gradient(90deg,var(--purple-deep) 0%,#4f1d6e 50%,var(--purple-bright) 100%)}
  .schedule-title{position:absolute;top:72px;left:0;width:1200px;text-align:center;font-family:"Poppins",sans-serif;font-weight:400;font-size:33px;color:#fff;line-height:44px}
  .field{position:absolute;top:138px;height:39px;background:#fff;font-size:12.5px;color:#555;line-height:39px;padding-left:15px}
  .field svg{position:absolute;right:12px;top:13px}
  .field-message{top:198px;left:133px;width:934px;height:127px;line-height:20px;padding-top:14px}
  .submit{position:absolute;left:550px;top:345px;width:100px;height:40px;background:var(--ink);color:#fff;font-family:"Poppins",sans-serif;font-size:14.5px;text-align:center;line-height:40px}

  /* footer */
  .site-footer{position:absolute;top:2410px;left:0;width:1200px;height:115px;background:var(--footer);color:#ccc}
  .footer-nav{position:absolute;left:133px;top:31px;font-size:12px;line-height:18px}
  .footer-nav a{color:#ddd;text-decoration:none}
  .footer-nav span{margin:0 8px;color:#aaa}
  .copyright{position:absolute;left:133px;top:60px;font-size:11.5px;color:#ccc;line-height:18px}
  .social{position:absolute;right:133px;top:48px;display:flex;gap:16px;font-size:12px;color:#bbb;line-height:18px}
</style>
</head>
<body>
<div class="page">

  <header class="site-header">
    <div class="brand">steady ledger</div>
    <nav class="main-nav">
      <a href="#" class="is-active">Home</a>
      <a href="#">About</a>
      <a href="#">Services</a>
      <a href="#">Schedule</a>
      <a href="#">Contact Us</a>
    </nav>
  </header>

  <section class="hero" role="img" aria-label="Video placeholder: a doctor in a white coat talking with a patient across a desk">
    <svg class="hero-play" width="60" height="60" viewBox="0 0 60 60" aria-hidden="true">
      <circle cx="30" cy="30" r="30" fill="#fff"/>
      <path d="M24 18 L42 30 L24 42 Z" fill="#555"/>
    </svg>
    <h1 class="hero-title">Vestibulum condimentum risus ut posuere</h1>
  </section>

  <section class="welcome">
    <h2 class="welcome-title">Welcome to Steady Ledger</h2>
    <p class="welcome-text">Maecenas vel tortor accumsan quam varius imperdiet vel eget elit. Aenean facilisis tincidunt lectus, id dictum nisi luctus eget. Vivamus efficitur ex condimentum, malesuada eros eget, feugiat nibh. Sed tellus ex, imperdiet eget gravida sit amet, volutpat eget turpis. In nec ultricies est. Etiam mattis augue vehicula odio posuere, sit amet tempus lectus luctus. Nulla facilisi. Etiam vel massa elementum, bibendum tellus venenatis, feugiat massa.</p>
    <a class="btn-soft welcome-btn" href="#">Read More</a>
    <div class="welcome-photo" role="img" aria-label="Photo of a smiling doctor seated at a desk in a bright clinic"></div>
  </section>

  <section class="services">
    <h2 class="section-title">Services</h2>

    <div class="service" style="left:137px">
      <svg width="66" height="68" viewBox="0 0 66 68" fill="none" stroke="#6b2a9c" stroke-width="2.2" aria-hidden="true">
        <rect x="4" y="8" width="44" height="56" rx="3"/>
        <rect x="10" y="14" width="32" height="12"/>
        <rect x="10" y="32" width="8" height="7"/><rect x="22" y="32" width="8" height="7"/><rect x="34" y="32" width="8" height="7"/>
        <rect x="10" y="44" width="8" height="7"/><rect x="22" y="44" width="8" height="7"/><rect x="34" y="44" width="8" height="13"/>
        <path d="M56 6 L62 6 L62 54 L59 62 L56 54 Z"/>
      </svg>
      <div class="service-name">ACCOUNTING</div>
      <p class="service-text">Maecenas vel tortor accumsan quam varius imperdiet vel eget elit</p>
    </div>

    <div class="service" style="left:375px">
      <svg width="70" height="68" viewBox="0 0 70 68" fill="none" stroke="#6b2a9c" stroke-width="2.2" aria-hidden="true">
        <path d="M4 18 L40 8 L46 26"/>
        <rect x="4" y="22" width="44" height="26" rx="2"/>
        <circle cx="26" cy="35" r="7"/>
        <ellipse cx="56" cy="40" rx="11" ry="4"/>
        <path d="M45 40 V62 M67 40 V62"/>
        <path d="M45 47 Q56 52 67 47 M45 54 Q56 59 67 54 M45 62 Q56 67 67 62"/>
      </svg>
      <div class="service-name">FINANCING</div>
      <p class="service-text">Maecenas vel tortor accumsan quam varius imperdiet vel eget elit</p>
    </div>

    <div class="service" style="left:614px">
      <svg width="72" height="66" viewBox="0 0 72 66" fill="none" stroke="#6b2a9c" stroke-width="2.2" aria-hidden="true">
        <path d="M30 6 H64 a6 6 0 0 1 6 6 V30 a6 6 0 0 1 -6 6 H60 L60 44 L52 36 H42"/>
        <path d="M8 24 H38 a6 6 0 0 1 6 6 V48 a6 6 0 0 1 -6 6 H18 L10 62 L10 54 H8 a6 6 0 0 1 -6 -6 V30 a6 6 0 0 1 6 -6 Z"/>
        <path d="M12 36 H34 M12 43 H28 M46 16 H60 M50 23 H60"/>
      </svg>
      <div class="service-name">CONSULTING</div>
      <p class="service-text">Maecenas vel tortor accumsan quam varius imperdiet vel eget elit</p>
    </div>

    <div class="service" style="left:851px">
      <svg width="64" height="68" viewBox="0 0 64 68" fill="none" stroke="#6b2a9c" stroke-width="2.2" aria-hidden="true">
        <path d="M4 8 L12 6 L12 62 L4 60 Z"/>
        <rect x="12" y="4" width="46" height="60" rx="2"/>
        <circle cx="33" cy="26" r="11"/>
        <path d="M33 15 V26 H44"/>
        <path d="M20 44 H50 M20 50 H44 M20 56 H38"/>
      </svg>
      <div class="service-name">ANALYZING</div>
      <p class="service-text">Maecenas vel tortor accumsan quam varius imperdiet vel eget elit</p>
    </div>
  </section>

  <section class="testimonials">
    <h2 class="section-title">Testimonials</h2>

    <article class="testimonial" style="left:133px">
      <div class="avatar" role="img" aria-label="Portrait photo of William"></div>
      <p class="quote">Mauris suscipit felis id nunc elementum varius. Praesent elementum nulla sit amet justo pellentesque scelerisque. Nam et tortor in ante iaculis porttitor in luctus mi.</p>
      <div class="author">- William</div>
      <div class="author-role">Vivamus gravida</div>
    </article>

    <article class="testimonial" style="left:453px">
      <div class="avatar" role="img" aria-label="Portrait photo of Emma" style="background:linear-gradient(160deg,#e8dcc4,#9a8a70)"></div>
      <p class="quote">Mauris suscipit felis id nunc elementum varius. Praesent elementum nulla sit amet justo pellentesque scelerisque. Nam et tortor in ante iaculis porttitor in luctus mi.</p>
      <div class="author">- Emma</div>
      <div class="author-role">Vivamus gravida</div>
    </article>

    <article class="testimonial" style="left:772px">
      <div class="avatar" role="img" aria-label="Portrait photo of Daniel" style="background:linear-gradient(160deg,#bdb3aa,#5e544c)"></div>
      <p class="quote">Mauris suscipit felis id nunc elementum varius. Praesent elementum nulla sit amet justo pellentesque scelerisque. Nam et tortor in ante iaculis porttitor in luctus mi.</p>
      <div class="author">- Daniel</div>
      <div class="author-role">Vivamus gravida</div>
    </article>

    <a class="btn-soft view-all" href="#">View All</a>
  </section>

  <section class="schedule">
    <h2 class="schedule-title">Schedule an Appointment</h2>
    <div class="field" style="left:133px;width:217px">Name</div>
    <div class="field" style="left:372px;width:217px">Email</div>
    <div class="field" style="left:609px;width:217px">Service for
      <svg width="12" height="10" viewBox="0 0 12 10" aria-hidden="true"><path d="M1 2 L6 8 L11 2" fill="none" stroke="#555" stroke-width="2"/></svg>
    </div>
    <div class="field" style="left:848px;width:219px">Date and Time
      <svg width="13" height="13" viewBox="0 0 13 13" aria-hidden="true"><rect x="0.5" y="2" width="12" height="10.5" fill="#555"/><rect x="2" y="5" width="9" height="6" fill="#fff"/><path d="M3 0 V3 M10 0 V3" stroke="#555" stroke-width="1.5"/><path d="M4.5 5 V11 M6.5 5 V11 M8.5 5 V11 M2 8 H11" stroke="#555" stroke-width=".8"/></svg>
    </div>
    <div class="field field-message">Message</div>
    <div class="submit">SUBMIT</div>
  </section>

  <footer class="site-footer">
    <nav class="footer-nav">
      <a href="#">Home</a><span>|</span><a href="#">About</a><span>|</span><a href="#">Services</a><span>|</span><a href="#">Schedule</a><span>|</span><a href="#">Contact Us</a>
    </nav>
    <p class="copyright">Copyright ©&nbsp; 2018&nbsp; Steady Ledger.&nbsp; All rights reserved.</p>
    <div class="social"><span>Linkup</span><span>Chirp</span></div>
  </footer>

</div>
</body>
</html>
```